IT Company Business Card design

Brisk Node is a new computer solutions business focusing on setting up servers and computer systems for small to medium sized businesses.

A business client will either request a solution, or support for a current system and we will turn up on site to provide these services.

We are bast in Christchurch, New Zealand.

We are looking for unique business card's that stand out and show off the business in a professional light.

Open to all idea's etc.

Industry/Entity Type

Computer

Requirements
Must have
• Business Logo (AI file attached)
Employee Name
Business title
Business landline number
Cell phone number
Email
Web URL
Nice to have
• Could be nice to have some keywords (possibly on the back) such as:

Business IT solutions
Network installations
Phone solutions
Server management
Software diagnostics

The above is not needed, just an idea.

```html
<!DOCTYPE html>
<html lang="en">
<head>
<meta charset="utf-8">
<title>Brisk Node business cards</title>
<link rel="stylesheet" href="https://fonts.googleapis.com/css2?family=Open+Sans:wght@400;600;700&family=Questrial&display=swap">
<style>
  :root {
    --page: #e6e6ec;
    --metal-light: #f1f1f1;
    --metal-mid: #d9d9d9;
    --metal-dark: #c4c4c4;
    --ink: #1d1d1f;
    --ink-soft: #3a3a3c;
    --navy: #1f2f78;
    --blue: #2f6fb8;
    --sky: #5cc0ec;
    --divider: #8c8c8c;
  }
  * { box-sizing: border-box; margin: 0; padding: 0; }
  html, body { width: 1200px; height: 987px; overflow: hidden; }
  body {
    background: var(--page);
    font-family: "Open Sans", sans-serif;
    color: var(--ink);
    position: relative;
  }
  .card {
    position: absolute;
    left: 270px;
    width: 660px;
    height: 377px;
    border-radius: 26px;
    background: linear-gradient(160deg, var(--metal-light) 0%, var(--metal-mid) 55%, var(--metal-dark) 100%);
    box-shadow: 0 10px 28px rgba(0,0,0,.14);
    overflow: hidden;
  }
  .card--back { top: 80px; }
  .card--front { top: 520px; }

  .brand {
    position: absolute;
    display: flex;
    align-items: flex-start;
  }
  .brand__dot {
    flex: none;
    border-radius: 50%;
    background: var(--blue);
  }
  .brand__rule {
    flex: none;
    width: 1px;
    background: var(--divider);
  }
  .brand__name {
    font-family: "Questrial", sans-serif;
    text-transform: uppercase;
    color: var(--ink);
    white-space: nowrap;
    line-height: 1;
  }

  .card--back .brand { left: 80px; top: 70px; }
  .card--back .brand__dot { width: 110px; height: 110px; }
  .card--back .brand__rule { height: 110px; margin: 30px 20px 0 22px; }
  .card--back .brand__name { font-size: 46px; letter-spacing: 4px; margin-top: 82px; }
  .card--back .web {
    position: absolute; left: 0; right: 0; top: 270px; text-align: center;
    font-weight: 700; font-size: 21px; letter-spacing: 7px; color: var(--ink-soft);
  }

  .card--front .tab {
    position: absolute; left: 0; top: 22px; width: 14px; height: 46px;
    background: linear-gradient(180deg, var(--navy), var(--sky));
  }
  .contact { position: absolute; left: 46px; top: 22px; }
  .contact__name { font-weight: 700; font-size: 24px; color: var(--navy); line-height: 1.1; }
  .contact__title { font-size: 15px; color: var(--ink-soft); margin-bottom: 22px; }
  .contact__address { font-size: 16px; line-height: 1.3; color: var(--ink-soft); margin-bottom: 16px; }
  .contact__line { display: flex; align-items: center; gap: 8px; font-size: 16px; line-height: 1.55; color: var(--ink-soft); }
  .contact__line svg { width: 14px; height: 14px; fill: var(--blue); }
  .card--front .web {
    position: absolute; left: 46px; top: 318px;
    font-weight: 700; font-size: 18px; letter-spacing: 2px; color: var(--ink);
  }
  .card--front .brand { left: 262px; top: 150px; }
  .card--front .brand__dot { width: 88px; height: 88px; }
  .card--front .brand__rule { height: 88px; margin: 26px 16px 0 18px; }
  .card--front .brand__name { font-size: 36px; letter-spacing: 3px; margin-top: 70px; }
</style>
</head>
<body>
  <section class="card card--back">
    <div class="brand">
      <div class="brand__dot"></div>
      <div class="brand__rule"></div>
      <div class="brand__name">Brisk Node</div>
    </div>
    <p class="web">www.brisknode.com</p>
  </section>

  <section class="card card--front">
    <div class="tab"></div>
    <div class="contact">
      <p class="contact__name">Employee Name</p>
      <p class="contact__title">Title</p>
      <p class="contact__address">00, Complex name<br>City, State 0042</p>
      <p class="contact__line">
        <svg viewBox="0 0 24 24" aria-hidden="true"><path d="M6.6 10.8a15 15 0 0 0 6.6 6.6l2.2-2.2a1 1 0 0 1 1-.25 11.4 11.4 0 0 0 3.6.57 1 1 0 0 1 1 1V20a1 1 0 0 1-1 1A17 17 0 0 1 3 4a1 1 0 0 1 1-1h3.5a1 1 0 0 1 1 1c0 1.250.2 2.450.57 3.57a1 1 0 0 1-.25 1z"/></svg>
        123 456 7890
      </p>
      <p class="contact__line">
        <svg viewBox="0 0 24 24" aria-hidden="true"><path d="M7 1h10a2 2 0 0 1 2 2v18a2 2 0 0 1-2 2H7a2 2 0 0 1-2-2V3a2 2 0 0 1 2-2zm0 3v14h10V4zm5 15.5a1 1 0 1 0 0 2 1 1 0 0 0 0-2z"/></svg>
        456 789 1234
      </p>
      <p class="contact__line">
        <svg viewBox="0 0 24 24" aria-hidden="true"><path d="M2 5h20v14H2zm2 2v.5l8 5 8-5V7zm0 2.8V17h16V9.8l-8 5z"/></svg>
        info@brisknode.com
      </p>
    </div>
    <p class="web">www.brisknode.com</p>
    <div class="brand">
      <div class="brand__dot"></div>
      <div class="brand__rule"></div>
      <div class="brand__name">Brisk Node</div>
    </div>
  </section>
</body>
</html>
```